Single Side Postcard Size Flyer Design

We want to design an attractive and eye-catching sign for hair stylists and barbers to sit on their workstations to attract the attention of their clients regarding hair loss and encourage them to speak to their stylist about it of they are would like to seek treatment.
Many men and women suffer from hair loss, but are often in denial it is happening or too embarrassed to talk about it.
This postcard sized flyer is designed to stick to the mirror at their hair stylist or barber and encourage them to ask their stylist about it.
We want this to be very plain and simple. With just perhaps some kind of simple head line and worry lines. I have uploaded a simple idea.
I have also uploaded the print templates that must be used to provide final designs.

Target Market(s)

Men aged 25 to 60 with thinning hair

Industry/Entity Type

Healthcare

Font styles to use
Sans Serif

Colors
0355a3
ffffff
cfcfcf
1b1b1b

Requirements
Must have
• Flyer size is vertical 4" x 6"
• Copy for the flyer is as follows ans is in color blue: #014ca5
• Worried About Thinning Hair?
• 2 out of 3 Men will have visible hair loss by age 35.
• The Good News is that your
• Barber or Stylist can tell you how to
• stop the loss & grow back your hair.
• Just ask.
• The Brisk Lattice Program from
• The Marlow Pine Company
• New Science. No Surgery. Your Hair.
• www.quellvantinfo.example
Should not have
• - dont add any logos, images or ornate design. this needs to be simple, easy to ready and eye catching.
• - do not use the color red in any capacity.

```html
<!DOCTYPE html>
<html lang="en">
<head>
<meta charset="utf-8">
<title>Worried About Thinning Hair? – Workstation Card</title>
<link rel="stylesheet" href="https://fonts.googleapis.com/css2?family=Arimo:wght@400;700&display=swap">
<style>
  :root {
    --brand-blue: #0355a3;
    --copy-blue: #014ca5;
    --white: #ffffff;
    --light-grey: #cfcfcf;
    --ink: #1b1b1b;
    --tone-light: #efe3da;
    --tone-mid: #d9b39c;
  }
  html, body {
    margin: 0;
    padding: 0;
    width: 800px;
    height: 1200px;
    overflow: hidden;
    background: var(--white);
  }
  .card {
    position: relative;
    width: 800px;
    height: 1200px;
    background: var(--brand-blue);
    font-family: "Arimo", Arial, sans-serif;
  }
  .card__upper {
    position: absolute;
    left: 17px;
    top: 16px;
    width: 766px;
    height: 844px;
    background: var(--white);
    text-align: center;
  }
  .headline {
    margin: 0;
    position: absolute;
    top: 44px;
    left: 0;
    width: 100%;
    font-weight: 700;
    color: var(--copy-blue);
  }
  .headline__lead {
    display: block;
    font-size: 76px;
    line-height: 76px;
  }
  .headline__tail {
    display: block;
    margin-top: 6px;
    font-size: 96px;
    line-height: 96px;
    letter-spacing: -0.5px;
  }
  .headline__plain {
    font-weight: 400;
    color: var(--ink);
  }
  .portrait-frame {
    position: absolute;
    left: 128px;
    top: 249px;
    width: 502px;
    height: 293px;
    box-sizing: border-box;
    border: 11px solid var(--brand-blue);
    background: var(--white);
    padding: 4px;
  }
  .portrait {
    width: 100%;
    height: 100%;
    background: linear-gradient(180deg, var(--tone-light) 0%, var(--tone-mid) 100%);
  }
  .stat-figure {
    position: absolute;
    top: 580px;
    left: 0;
    width: 100%;
    margin: 0;
    font-size: 32px;
    line-height: 36px;
    font-weight: 700;
    color: var(--copy-blue);
  }
  .stat-detail {
    position: absolute;
    top: 622px;
    left: 0;
    width: 100%;
    margin: 0;
    font-size: 25px;
    line-height: 30px;
    color: var(--ink);
  }
  .good-news {
    position: absolute;
    top: 666px;
    left: 0;
    width: 100%;
    margin: 0;
    font-size: 25px;
    line-height: 42px;
    color: var(--ink);
  }
  .call-to-action {
    position: absolute;
    top: 860px;
    left: 0;
    width: 800px;
    height: 97px;
    margin: 0;
    line-height: 97px;
    text-align: center;
    font-size: 66px;
    font-weight: 700;
    color: var(--white);
  }
  .program-box {
    position: absolute;
    left: 28px;
    top: 957px;
    width: 744px;
    height: 159px;
    box-sizing: border-box;
    background: var(--white);
    text-align: center;
    padding-top: 18px;
  }
  .program-box__name {
    margin: 0;
    font-size: 27px;
    line-height: 37px;
    color: var(--ink);
  }
  .program-box__promise {
    margin: 0;
    padding-top: 5px;
    font-size: 41px;
    line-height: 46px;
    font-weight: 700;
    color: var(--copy-blue);
  }
  .web-address {
    position: absolute;
    left: 0;
    top: 1134px;
    width: 800px;
    margin: 0;
    text-align: center;
    font-size: 31px;
    line-height: 36px;
    font-weight: 700;
    color: var(--white);
  }
</style>
</head>
<body>
  <main class="card">
    <section class="card__upper">
      <h1 class="headline">
        <span class="headline__lead">Worried About</span>
        <span class="headline__tail"><span class="headline__plain">Thinning</span> Hair?</span>
      </h1>
      <div class="portrait-frame">
        <div class="portrait" role="img" aria-label="Photo of a balding man's head, cropped at the brow"></div>
      </div>
      <p class="stat-figure">2 out of 3 Men</p>
      <p class="stat-detail">will have visible hair loss by age 35.</p>
      <p class="good-news">The Good News is that your Barber<br>or Stylist can tell you how to stop<br>the loss &amp; grow back your hair.</p>
    </section>
    <p class="call-to-action">Just ask.</p>
    <section class="program-box">
      <p class="program-box__name">The Brisk Lattice Program<br>from The Marlow Pine Company</p>
      <p class="program-box__promise">New Science. No Surgery. Your Hair.</p>
    </section>
    <p class="web-address">www.quellvantinfo.example</p>
  </main>
</body>
</html>
```